Flyer Design for sewing business

Hi. i need flyers for my new business called " Telvo Designs". I am based in Sauchie. I offer Door to Door Clothing Alteration Service!
I provide a door to door alteration service for Clackmannanshire area with 20 miles radiance! (I give free consultations at your preferred location where I can accurately quote the cost of the alteration, as this depends on the garment itself. I aim to deliver the completed item back to you within a week though often it is less than this.)
I also design and sew occasional girls dresses ( first communion, flower girl, party dresses)
The consultation are free with no commitment to take the service.

I wold like see designs that use colors similar to colors on my website, like dusty pink, orange.

To contact either phone RUTH 07913284406
or email: ruth.marsk71@quillbox.com

www.pagebook.com/telvodesigns
www.telvo-designs.sitenest.com

THAT IS THE Price List Jeans/Trousers: Shorten....................................from £10.00 Taken in (waist).......................from £8.00 Taken in (side seams)..............from £10.00 Replace zip...............................from £10.00 Dresses/Skirts: Shorten....................................from £10.00 Taken in (waist).......................from £8.00 Taken in (side seams)..............from £8.00 Replace zip...............................from £10.00 Jacket/Coat: Shorten sleeves........................from £12.00 Shorten length (Jacket)...........from £16.00 Shorten length (Coat)..............from £18.00 Taken in (back seam)...............from £12.00 Taken in (side seams)..............from £18.00 Repairs......................................from £5.00 Bridal: Shorten Wedding Dress...........from £25.00 All other bridal alteration quotes can be given on consultation.

Reason: HI, ALL! IN THE NEXT FEW DAYS I GONE EXPERIENCE HOUSE MOVE AND SOME STRESS INVOLVING IN THIS.THANK YOU ALL FOR UNDERSTANDING AND A PATIENCE!

Industry/Entity Type

Business

```html
<!DOCTYPE html>
<html lang="en">
<head>
<meta charset="utf-8">
<title>Telvo Designs – Door to Door Clothing Alteration Service</title>
<link href="https://fonts.googleapis.com/css2?family=Oswald:wght@300;400;700&family=Roboto+Condensed:ital,wght@0,400;0,700;1,400;1,700&display=swap" rel="stylesheet">
<style>
:root{
  --red:#ee3d43;
  --red-dark:#d8262e;
  --blush:#f7dbe0;
  --ink:#4a3a3c;
  --white:#ffffff;
}
*{margin:0;padding:0;box-sizing:border-box}
html,body{width:849px;height:1200px;overflow:hidden;background:#fff}
.flyer{position:relative;width:849px;height:1200px;overflow:hidden;
  background:linear-gradient(180deg,var(--blush) 0%,#fbeef0 100%);font-family:"Roboto Condensed",sans-serif;color:var(--ink)}
.masthead{position:absolute;left:0;top:0;width:849px;height:362px;background:var(--red);text-align:center;color:var(--white);font-family:"Oswald",sans-serif}
.masthead .line1{position:absolute;left:0;right:0;top:28px;font-weight:700;font-size:112px;line-height:1}
.masthead .line2{position:absolute;left:0;right:0;top:140px;font-weight:700;font-size:112px;line-height:1}
.masthead .line3{position:absolute;left:0;right:0;top:252px;font-weight:300;font-size:96px;line-height:1}
.mannequin{position:absolute;left:300px;top:362px;width:350px;height:748px;
  background:linear-gradient(180deg,#f3d3d9 0%,#e8c2b4 55%,#d9b09a 100%)}
.prices{position:absolute;left:24px;top:368px;width:342px;height:700px;background:var(--white);padding:14px 16px}
.prices h2{font-family:"Oswald",sans-serif;font-weight:400;color:var(--red);font-size:48px;text-align:center;line-height:1;margin-bottom:16px}
.prices h3{font-family:"Oswald",sans-serif;font-weight:400;color:var(--red);font-size:27px;line-height:1.15;margin-top:12px}
.row{display:flex;align-items:baseline;font-size:15px;line-height:26px}
.row .dots{flex:1;border-bottom:2px dotted #b9a7a9;margin:0 3px;transform:translateY(-4px)}
.row .price{white-space:nowrap}
.row .price b{color:var(--red);font-size:20px}
.consult{position:absolute;left:495px;top:380px;width:335px;text-align:center}
.consult h2{font-style:italic;font-weight:700;color:var(--red);font-size:46px;line-height:1.05;transform:rotate(-4deg)}
.consult p{font-style:italic;color:var(--red-dark);font-size:31px;line-height:1.2;margin-top:14px}
.consult p+p{margin-top:30px}
.badge{position:absolute;left:382px;top:850px;width:200px;height:200px;border-radius:50%;background:var(--red);color:var(--white);text-align:center;
  display:flex;flex-direction:column;align-items:center;justify-content:center}
.badge .small{font-size:22px;font-weight:700;line-height:1.1}
.badge .big{font-size:24px;font-weight:700;line-height:1.15;white-space:nowrap}
.badge .note{font-size:15px;line-height:1.15;margin-top:4px}
.footer{position:absolute;left:0;bottom:0;width:849px;height:90px;background:var(--red);color:var(--white);display:flex;align-items:center;justify-content:center;gap:14px;font-size:25px;font-weight:700}
</style>
</head>
<body>
<div class="flyer">
  <header class="masthead">
    <div class="line1">Door to Door</div>
    <div class="line2">Clothing</div>
    <div class="line3">Alteration Service</div>
  </header>

  <div class="mannequin" role="img" aria-label="Photo of a dressmaker's mannequin draped with a pink tape measure and scissors"></div>

  <section class="prices">
    <h2>Price List</h2>
    <h3>Jeans/Trousers:</h3>
    <div class="row"><span>Shorten</span><span class="dots"></span><span class="price">from <b>£10.00</b></span></div>
    <div class="row"><span>Taken in (waist)</span><span class="dots"></span><span class="price">from <b>£8.00</b></span></div>
    <div class="row"><span>Taken in (side seams)</span><span class="dots"></span><span class="price">from <b>£10.00</b></span></div>
    <div class="row"><span>Replace zip</span><span class="dots"></span><span class="price">from <b>£10.00</b></span></div>
    <h3>Dresses/Skirts:</h3>
    <div class="row"><span>Shorten</span><span class="dots"></span><span class="price">from <b>£10.00</b></span></div>
    <div class="row"><span>Taken in (waist)</span><span class="dots"></span><span class="price">from <b>£8.00</b></span></div>
    <div class="row"><span>Taken in (side seams)</span><span class="dots"></span><span class="price">from <b>£8.00</b></span></div>
    <div class="row"><span>Replace zip</span><span class="dots"></span><span class="price">from <b>£10.00</b></span></div>
    <h3>Jacket/Coat:</h3>
    <div class="row"><span>Shorten sleeves</span><span class="dots"></span><span class="price">from <b>£12.00</b></span></div>
    <div class="row"><span>Shorten length (Jacket)</span><span class="dots"></span><span class="price">from <b>£16.00</b></span></div>
    <div class="row"><span>Shorten length (Coat)</span><span class="dots"></span><span class="price">from <b>£18.00</b></span></div>
    <div class="row"><span>Taken in (back seam)</span><span class="dots"></span><span class="price">from <b>£12.00</b></span></div>
    <div class="row"><span>Taken in (side seams)</span><span class="dots"></span><span class="price">from <b>£18.00</b></span></div>
    <div class="row"><span>Repairs</span><span class="dots"></span><span class="price">from <b>£5.00</b></span></div>
    <h3>Bridal:</h3>
    <div class="row"><span>Shorten Wedding Dress</span><span class="dots"></span><span class="price">from <b>£25.00</b></span></div>
  </section>

  <section class="consult">
    <h2>Free<br>Consultations</h2>
    <p>at your preferred location where I can accurately quote the cost of the alteration, as this depends on the garment itself.</p>
    <p>My aim to deliver the completed item back to you within a week, though often it is less than this.</p>
  </section>

  <div class="badge">
    <div class="small">All other</div>
    <div class="big">bridal Alteration</div>
    <div class="big">Quotes</div>
    <div class="note">can be given on<br>consultation</div>
  </div>

  <footer class="footer">
    <span>www.pagebook.com/telvodesigns</span><span>|</span><span>www.telvo-designs.sitenest.com</span>
  </footer>
</div>
</body>
</html>
```